Healthy Meal Delivery Website Needs to be updated, current, fresh and modern

Hi there,

The current website i have is super old and outdated.

I would like a beautiful modern site that has all the same content as the previous except with a a new, modern and trustworthy feel.

The current website is https://pelvarobistro.com/

Target Market(s)

Health Conscious Young Professionals

Industry/Entity Type

Food Service

Font styles to use
Sans Serif

Requirements
Must have
• Modern Trustworthy feel
Should not have
• Anything out dated or cheesy or scammy

```html
<!DOCTYPE html>
<html lang="en">
<head>
<meta charset="utf-8">
<title>Pelvaro Bistro</title>
<link href="https://fonts.googleapis.com/css2?family=Cabin:wght@400;600;700&family=Open+Sans:wght@400;600;700&display=swap" rel="stylesheet">
<style>
:root{
  --yellow:#f5e51b;
  --ink:#111111;
  --night:#161616;
  --panel:#1d1d1d;
  --paper:#f1f1f1;
  --white:#ffffff;
  --muted:#9a9a9a;
  --blue:#2fa8e0;
  --text:#333333;
}
*{box-sizing:border-box;margin:0;padding:0}
html,body{width:1200px;height:2764px;overflow:hidden}
body{font-family:"Open Sans",Arial,sans-serif;color:var(--text);background:var(--ink);position:relative}
h1,h2,h3,.heading{font-family:"Cabin",Arial,sans-serif}
section,header,footer{position:absolute;left:0;width:1200px}

/* header */
.site-header{top:0;height:56px;background:rgba(10,10,10,.85);z-index:3;display:flex;align-items:center;padding:0 140px}
.brand{display:flex;align-items:center;gap:10px;font-family:"Cabin",sans-serif;font-weight:700;font-size:22px;color:var(--yellow)}
.brand-mark{width:20px;height:20px;background:var(--yellow)}
.main-nav{margin-left:auto;display:flex;gap:26px;font-size:13px;color:#ddd}
.main-nav .active{color:var(--yellow)}
.nav-tools{display:flex;gap:18px;margin-left:30px}
.nav-tools span{width:10px;height:10px;border:2px solid #ddd;border-radius:50%}

/* hero */
.hero{top:0;height:760px}
.hero-photo{position:absolute;inset:0;background:radial-gradient(ellipse at 62% 55%,#e9e2cf 0%,#b9a77a 18%,#5b6b2b 32%,#2a2419 55%,#0c0b09 80%)}
.hero-copy{position:absolute;left:120px;top:310px;color:var(--white)}
.hero-copy h1{font-size:56px;font-weight:700;letter-spacing:1px}
.hero-copy p{font-size:14px;max-width:430px;margin-top:8px;color:#eee}
.btn{display:inline-block;background:var(--yellow);color:var(--ink);font-weight:600;font-size:14px;padding:10px 26px}
.hero-copy .btn{margin-top:26px}
.arrow{position:absolute;top:50%;width:30px;height:60px;margin-top:-30px}
.arrow.left{left:40px}.arrow.right{right:40px}
.dots{position:absolute;left:0;right:0;bottom:28px;display:flex;justify-content:center;gap:10px}
.dots i{width:10px;height:10px;border-radius:50%;background:rgba(255,255,255,.5)}
.dots i:first-child{background:var(--white)}

/* perks */
.perks{top:760px;height:140px;background:var(--ink);display:flex;justify-content:center;gap:150px;align-items:center}
.perk{display:flex;gap:14px;align-items:center;color:var(--white)}
.perk h3{font-size:18px}
.perk p{font-size:11px;color:var(--muted)}

/* menu */
.menu-intro{top:900px;height:160px;background:var(--paper);text-align:center;padding-top:50px}
.menu-intro h2{font-size:34px;color:#444;font-weight:600}
.menu-intro p{font-size:12px;color:#777;max-width:640px;margin:10px auto 0}
.menu-strip{top:1060px;height:260px;display:flex}
.dish{flex:1;position:relative}
.dish .name{position:absolute;right:20px;bottom:40px;text-align:right;color:var(--white)}
.dish .name strong{font-family:"Cabin",sans-serif;font-size:30px;display:block}
.dish .name small{font-size:11px}
.dish.dinner{background:linear-gradient(135deg,#4a3e2c,#1e1a13)}
.dish.breakfast{background:linear-gradient(135deg,#d6cfc0,#7d6f58)}
.dish.lunch{background:linear-gradient(135deg,#8a6a3a,#3f5a22)}
.dish.snack{background:linear-gradient(135deg,#5f4b35,#221d18)}

/* delivery */
.delivery{top:1320px;height:480px;background:var(--night);text-align:center;color:var(--white)}
.delivery h2{font-size:32px;font-weight:600;padding-top:36px;line-height:1.35}
.delivery h2 em{font-style:normal;color:var(--blue)}
.delivery .lead{font-size:12px;color:#bbb;margin-top:10px}
.features{display:flex;justify-content:center;gap:44px;margin-top:40px}
.feature{width:180px;height:270px;background:var(--white);color:var(--text);padding:24px 16px}
.feature.highlight{background:var(--yellow)}
.feature h3{font-size:13px;font-weight:700;margin-top:12px;letter-spacing:1px}
.feature p{font-size:11px;margin-top:10px;line-height:1.5;color:#555}
.feature .more{display:block;font-size:11px;margin-top:22px;font-weight:600}

/* testimonials */
.testimonials{top:1800px;height:340px;background:var(--paper);text-align:center}
.testimonials h2{font-size:32px;font-weight:600;color:#444;padding-top:56px}
.testimonials blockquote{font-size:13px;color:#666;max-width:680px;margin:32px auto 0;line-height:1.7;font-style:italic}
.testimonials cite{display:block;font-style:normal;margin-top:24px;font-weight:700;color:#444}
.testimonials .arrow{top:170px}

/* newsletter */
.newsletter{top:2140px;height:360px;background:var(--night);text-align:center;color:var(--white)}
.newsletter h2{font-size:32px;font-weight:600;padding-top:56px;line-height:1.35}
.newsletter p{font-size:12px;color:#bbb;margin-top:14px}
.signup{display:flex;justify-content:center;margin-top:34px}
.signup .field{width:320px;height:40px;background:var(--white);color:#999;font-size:12px;text-align:left;padding:12px 14px}
.signup .btn{height:40px;padding:11px 28px}

/* footer */
.site-footer{top:2500px;height:220px;background:var(--ink);display:flex;gap:70px;padding:26px 120px 0;color:#ccc;font-size:12px}
.site-footer h3{color:var(--yellow);font-size:17px;margin-bottom:12px}
.col{width:200px}
.col li{list-style:none;line-height:1.7}
.contact-line{display:flex;gap:8px;align-items:center;margin-bottom:8px}
.form-field{height:22px;background:var(--white);margin-bottom:8px}
.form-field.tall{height:50px}
.form-row{display:flex;gap:8px}
.form-row .form-field{flex:1}
.col .btn{padding:4px 14px;font-size:11px}
.share{display:flex;gap:8px;margin-top:10px}
.share span{background:#3b3b3b;color:#fff;font-size:10px;padding:3px 8px}
.legal{position:absolute;top:2720px;left:0;width:1200px;height:44px;background:#0a0a0a;color:#888;font-size:11px;display:flex;justify-content:space-between;align-items:center;padding:0 120px}
</style>
</head>
<body>

<header class="site-header">
  <div class="brand"><span class="brand-mark"></span>Pelvaro Bistro</div>
  <nav class="main-nav">
    <span class="active">Home</span><span>Pelvaro Meal Plans</span><span>Menu</span><span>Pricing</span><span>About</span><span>Press</span><span>Contact</span>
  </nav>
  <div class="nav-tools"><span></span><span></span><span></span></div>
</header>

<section class="hero">
  <div class="hero-photo" role="img" aria-label="Plate of pasta with broccoli and cherry tomatoes"></div>
  <div class="hero-copy">
    <h1>Fresh and so Delicious</h1>
    <p>Balanced chef-made meals cooked fresh each morning and delivered chilled to your door, ready to heat.</p>
    <span class="btn">Order Now</span>
  </div>
  <svg class="arrow left" viewBox="0 0 30 60"><polyline points="24,4 6,30 24,56" fill="none" stroke="#f5e51b" stroke-width="5"/></svg>
  <svg class="arrow right" viewBox="0 0 30 60"><polyline points="6,4 24,30 6,56" fill="none" stroke="#f5e51b" stroke-width="5"/></svg>
  <div class="dots"><i></i><i></i><i></i><i></i><i></i></div>
</section>

<section class="perks">
  <div class="perk">
    <svg width="44" height="30" viewBox="0 0 44 30"><rect x="1" y="4" width="26" height="18" fill="#f5e51b"/><path d="M27 10h10l6 7v5H27z" fill="#f5e51b"/><circle cx="10" cy="25" r="4" fill="#fff"/><circle cx="35" cy="25" r="4" fill="#fff"/></svg>
    <div><h3>Free Shipping</h3><p>Local delivery at no extra fee</p></div>
  </div>
  <div class="perk">
    <svg width="34" height="34" viewBox="0 0 34 34"><path d="M5 20v-4a12 12 0 0 1 24 0v4" fill="none" stroke="#f5e51b" stroke-width="3"/><rect x="2" y="18" width="7" height="11" fill="#f5e51b"/><rect x="25" y="18" width="7" height="11" fill="#f5e51b"/></svg>
    <div><h3>Premium Support</h3><p>24/7 customer service</p></div>
  </div>
  <div class="perk">
    <svg width="40" height="28" viewBox="0 0 40 28"><rect x="1" y="1" width="38" height="26" rx="3" fill="none" stroke="#f5e51b" stroke-width="3"/><rect x="1" y="7" width="38" height="5" fill="#f5e51b"/></svg>
    <div><h3>Payment Method</h3><p>Cash on delivery</p></div>
  </div>
</section>

<section class="menu-intro">
  <h2>Select From Over 100 Menu Items</h2>
  <p>Pick dishes you love from a rotating menu built by our chefs and dietitians, then choose when you want them delivered.</p>
</section>

<section class="menu-strip">
  <div class="dish dinner" role="img" aria-label="Dinner dishes on a table"><div class="name"><strong>Dinner</strong><small>Grilled fish and roasted greens</small></div></div>
  <div class="dish breakfast" role="img" aria-label="Breakfast plate"><div class="name"><strong>Breakfast</strong><small>Oats, eggs and fresh fruit</small></div></div>
  <div class="dish lunch" role="img" aria-label="Lunch salad bowl"><div class="name"><strong>Lunch</strong><small>Hearty bowls and salads</small></div></div>
  <div class="dish snack" role="img" aria-label="Snack plate"><div class="name"><strong>Snack</strong><small>Fresh bites with cottage cheese</small></div></div>
</section>

<section class="delivery">
  <h2>The PELVARO <em>Delivers</em> Diet Meals To Your Door<br>In Toronto, GTA &amp; Montreal</h2>
  <p class="lead">Your food and delicious diet meals made with fresh ingredients that nourish your body.<br>Why not let us prepare your meals while you lose the weight?</p>
  <div class="features">
    <div class="feature">
      <svg width="40" height="40" viewBox="0 0 40 40"><circle cx="20" cy="20" r="18" fill="none" stroke="#333" stroke-width="2"/><polyline points="12,21 18,27 29,14" fill="none" stroke="#333" stroke-width="3"/></svg>
      <h3>HEALTHY</h3>
      <p>Every meal is portioned and balanced so you can eat well and feel your best all week long.</p>
      <span class="more">READ MORE...</span>
    </div>
    <div class="feature highlight">
      <svg width="40" height="40" viewBox="0 0 40 40"><circle cx="20" cy="20" r="18" fill="none" stroke="#333" stroke-width="2"/><polyline points="12,21 18,27 29,14" fill="none" stroke="#333" stroke-width="3"/></svg>
      <h3>CHOICES</h3>
      <p>Choose from breakfast, lunch, dinner and snacks, with new dishes added to the menu every week.</p>
      <span class="more">READ MORE...</span>
    </div>
    <div class="feature">
      <svg width="40" height="40" viewBox="0 0 40 40"><circle cx="20" cy="20" r="18" fill="none" stroke="#333" stroke-width="2"/><polyline points="12,21 18,27 29,14" fill="none" stroke="#333" stroke-width="3"/></svg>
      <h3>FRESH</h3>
      <p>Cooked from local produce each morning and prepared for you to reheat and enjoy.</p>
      <span class="more">READ MORE...</span>
    </div>
    <div class="feature">
      <svg width="40" height="40" viewBox="0 0 40 40"><circle cx="20" cy="20" r="18" fill="none" stroke="#333" stroke-width="2"/><polyline points="12,21 18,27 29,14" fill="none" stroke="#333" stroke-width="3"/></svg>
      <h3>CUSTOMIZED</h3>
      <p>Plans tailored to your goals, allergies and taste, adjusted to your level of activity.</p>
      <span class="more">READ MORE...</span>
    </div>
  </div>
</section>

<section class="testimonials">
  <h2>What Clients Say's</h2>
  <blockquote>"Honestly the best thing I have done for my health this year. The meals arrive on time, taste homemade and I never have to think about what to cook after work."</blockquote>
  <cite>Marla</cite>
  <svg class="arrow left" viewBox="0 0 30 60"><polyline points="24,4 6,30 24,56" fill="none" stroke="#f5e51b" stroke-width="5"/></svg>
  <svg class="arrow right" viewBox="0 0 30 60"><polyline points="6,4 24,30 6,56" fill="none" stroke="#f5e51b" stroke-width="5"/></svg>
</section>

<section class="newsletter">
  <h2>The PELVARO Is Based On Real Foods Made With<br>Fresh And Natural Ingredients.</h2>
  <p>It's about eating the freshest produce and whole grains that keep you full, with lean proteins and healthy fats.</p>
  <div class="signup"><span class="field">E-Mail Address</span><span class="btn">Subscribe</span></div>
</section>

<footer class="site-footer">
  <div class="col">
    <h3>Quick Link</h3>
    <ul><li>Home</li><li>Pelvaro Meal Plans</li><li>Menu</li><li>Pricing</li><li>About</li><li>Press</li><li>Contact</li></ul>
  </div>
  <div class="col">
    <h3>Stay In Touch</h3>
    <div class="contact-line"><svg width="12" height="12" viewBox="0 0 12 12"><path d="M2 1l3 3-1.5 1.5a7 7 0 0 0 3 3L8 7l3 3-2 2C4 12 0 8 0 3z" fill="#f5e51b"/></svg>+1 (555) 014-2290</div>
    <div class="contact-line"><svg width="12" height="10" viewBox="0 0 12 10"><rect x="0" y="0" width="12" height="10" fill="#f5e51b"/><polyline points="0,0 6,5 12,0" fill="none" stroke="#111"/></svg>hello@pelvarobistro.com</div>
    <div class="share"><span>Like</span><span>Share</span></div>
  </div>
  <div class="col">
    <h3>What Is Pelvaro?</h3>
    <p style="line-height:1.6">Pelvaro Bistro is a Toronto and Montreal kitchen cooking fresh diet meals for busy people. Meals are cooked daily and delivered to your door.</p>
  </div>
  <div class="col">
    <h3>Quick Contact</h3>
    <div class="form-row"><div class="form-field"></div><div class="form-field"></div></div>
    <div class="form-field tall"></div>
    <span class="btn">Send</span>
  </div>
</footer>
<div class="legal"><span>© Copyright 2020 Pelvaro Bistro · Individual</span><span>Privacy Policy · Terms &amp; conditions</span></div>

</body>
</html>
```